Motivational Poster Series for Students at Truck Driving School

We are looking for a series of 3 motivational posters (18"X 24") to be used in classrooms at a truck driving school. The audience for the posters will be the students that are currently in school and the purpose of the posters is to be motivational pieces that will be displayed on the walls.

We have provided the quotes below that are to be used on each poster. We have also provided some example images from PixVaultImages to give an idea on the backgrounds that we'd like to see on each poster. The images do not have to be exact, these are just examples of what we think will look good for each quote. Since this is a series, they can all be somewhat similar in look/feel - just with different images and quotes.

So, the basic idea is a background image/design with a quote being the main point of emphasis. Other than that, we would like to include the logo provided at a small scale in one of the corners of the poster as a watermark for branding purposes.

Below are the quotes for each of the 3 posters:

Poster 1 - “It’s very difficult to follow our dreams, but it’s even more difficult to forget them.” - Devan Okafor

Poster 2 - “Success doesn’t just come and find you, you have to go out and get it.” - Unknown

Poster 3 - “If you are not willing to learn, no one can help you. If you are determined to learn, no one can stop you.”
- Unknown

NOTE: these posters should be designed as 18" X 24" in size with 2 of them being landscape and one being portrait orientation (as shown in images provided below)

Below are some sample images to give an idea on what could be used as background design for each quote. The logo that should be used as a watermark in a corner for some subtle branding has been provided as well.

Target Market(s)

The target market for this series are truck drivers between the ages of 25-55. Mostly males.

Industry/Entity Type

Landscape

Requirements
Must have
• Quote featured, high quality background design/image, logo watermark

```html
<!DOCTYPE html>
<html lang="en">
<head>
<meta charset="utf-8">
<title>Poster – Willing to Learn</title>
<link rel="stylesheet" href="https://fonts.googleapis.com/css2?family=Roboto+Condensed:wght@300;700&display=swap">
<style>
  :root {
    --sky-top: #5e5a56;
    --sky-low: #6e5f55;
    --tree-dark: #1f1d1b;
    --road-glow: #e9c28c;
    --road-grey: #3b3633;
    --ground-dark: #242120;
    --trail-red: #d8352e;
    --band-red: #d23a35;
    --veil-grey: rgba(228, 228, 228, 0.8);
    --ink-white: #ffffff;
    --ink-dark: #1a1a1a;
  }
  html, body {
    margin: 0;
    padding: 0;
    width: 1200px;
    height: 900px;
    overflow: hidden;
    background: #ffffff;
  }
  .poster {
    position: relative;
    width: 1200px;
    height: 900px;
    overflow: hidden;
    font-family: "Roboto Condensed", "Arial Narrow", sans-serif;
  }
  .poster__photo {
    position: absolute;
    inset: 0;
    background:
      radial-gradient(ellipse 380px 520px at 930px 780px, rgba(216, 53, 46, 0.85), rgba(216, 53, 46, 0.35) 55%, transparent 80%),
      radial-gradient(ellipse 260px 300px at 1120px 760px, rgba(40, 48, 30, 0.7), transparent 75%),
      radial-gradient(ellipse 560px 40px at 760px 440px, rgba(233, 194, 140, 0.85), transparent 75%),
      radial-gradient(ellipse 420px 60px at 420px 520px, rgba(233, 194, 140, 0.55), transparent 75%),
      radial-gradient(ellipse 300px 90px at 1080px 330px, rgba(150, 100, 80, 0.55), transparent 75%),
      linear-gradient(180deg,
        var(--sky-top) 0%,
        #5a5350 20%,
        var(--sky-low) 30%,
        var(--tree-dark) 34%,
        var(--tree-dark) 45%,
        #4a3d33 48%,
        var(--road-grey) 55%,
        #2e2a27 70%,
        var(--ground-dark) 100%);
  }
  .poster__shapes {
    position: absolute;
    inset: 0;
  }
  .quote {
    position: absolute;
    top: 22px;
    left: 520px;
    width: 685px;
    margin: 0;
    text-align: center;
    color: var(--ink-white);
    font-weight: 300;
    font-size: 60px;
    line-height: 60px;
  }
  .quote__line { display: block; }
  .quote__strong {
    font-weight: 700;
    text-transform: uppercase;
    font-size: 57px;
  }
  .quote__author {
    display: block;
    font-weight: 300;
  }
  .brand {
    position: absolute;
    left: 100px;
    top: 560px;
    display: flex;
    align-items: center;
    gap: 12px;
    transform-origin: left top;
    transform: rotate(90deg);
    color: var(--ink-dark);
    font-weight: 700;
    font-size: 24px;
    letter-spacing: 0.5px;
    white-space: nowrap;
  }
  .brand__mark {
    width: 18px;
    height: 18px;
    background: var(--band-red);
  }
</style>
</head>
<body>
  <main class="poster">
    <div class="poster__photo" role="img" aria-label="Dusk highway photograph with long-exposure white and red vehicle light trails curving into the distance beside a dark tree line"></div>

    <svg class="poster__shapes" width="1200" height="900" viewBox="0 0 1200 900" aria-hidden="true">
      <path class="veil" d="M0,0 L35,0 C80,420 300,780 640,900 L0,900 Z" fill="var(--veil-grey)"/>
      <path class="curve-band" d="M35,0 L52,0 C110,420 400,820 830,900 L640,900 C300,780 80,420 35,0 Z" fill="var(--band-red)"/>
    </svg>

    <p class="quote">
      <span class="quote__line">If you are not</span>
      <span class="quote__line quote__strong">Willing to learn</span>
      <span class="quote__line">no one can help you. If you</span>
      <span class="quote__line">are determined to learn,</span>
      <span class="quote__line quote__strong">No one can stop you.</span>
      <span class="quote__author">— Unknown —</span>
    </p>

    <div class="brand">
      <span class="brand__mark"></span>
      <span class="brand__name">Roadway Driver Academy</span>
    </div>
  </main>
</body>
</html>
```